Web Design Project

Brightwater Digital owns and operates a large number of editorial websites. These websites provides mostly consumers in the financial services space with information and price comparisons for a particular service.

Brightwater Digital, as the holding company for each of these sites, currently has no website. We need to build a website targeted towards potential partners for our websites. The idea being that when we start a conversation with a partner, they can view our site and obtain some basic information about who we are.

The structure of the site is to be very simple, containing only a brief description about who we are, our contact details and a list of some of our websites:
• CoverQuest.net.au
• AutoPolicyMatcher.com.au
• NestPolicyMatcher.com.au
• WellPolicyMatcher.com.au
• CoverQuestMatcher.com.au
• TripPolicyMatcher.com.au
• CritterPolicyMatcher.com.au
• CashAdvanceMatcher.com.au
• MobileCoolingUnit.com.au
• FixedSaverYields.com.au
• ThriftyHabits.com.au
• PurseGran.com.au
• TameThePlastic.com.au
• PurseMinder.com.au
• ThirdPartyClaimsCoverOzland.com.au
• Trade-Protect.com.au
• AutoPolicyProviders.com.au
• WellPolicyProviders.com.au
• NestPolicyOzland.com
• CoverQuestOzland.com
• WageShieldPolicyOzland.com
• WellPolicyOzland.com
• CritterPolicyOzland.com
• CashAdvancesOzland.com
• PlasticPaysOzland.com
• NestLendersOzland.com
• NestEggFunds.net.au

The design of the site should say 'Internet company', 'professional', 'fresh thinking'. The design should not look like a corporate site that you would see from any corporate services business with images of people in suits. We are ultimately an Internet business and there should be a unique feel to the site.

We are open to a suggestion of a colour pallet as the holding company does not have an established logo.

Some sites that we like are:

http://www.prismwork-studio.co.uk/#home
http://sample00.layoutvault.example/wt_48248/index.html
http://sample00.layoutvault.example/wordpress_46388/
http://mindvolt.example/
http://www.tandora.us/
http://www.kelvorabintu.example/
http://www.slickfrontpages.example/Corporate/design-ideas-detail.html?id=7916
http://trebla.example/
http://orvantek.example/

Reason: Hi all, Apologies, but I need to extend the timeline. One of our key stakeholders is away for the next week. There are a few good designs that we have received to date and there are some tweaks that we would like to see before making a final decision. Thank you to everyone that has submitted designs - Have a great new year. Derek

Reason: Sorry to have to delay the deadline on this, but we did not find anything in the designs really resonated with us. We will have a further think about the existing designs that have been submitted and how we can provide more specific feedback to the designers to make some modifications to the designs.

Target Market(s)

We are targeting insurance companies / brokers that we are talking to. The idea is that we show a professional face to them.

Industry/Entity Type

Financial

Requirements
Must have
• Home Page (possibly integrated with About us details)
Contact Us
Our Sites

```html
<!DOCTYPE html>
<html lang="en">
<head>
<meta charset="utf-8">
<title>Brightwater Digital</title>
<link rel="stylesheet" href="https://fonts.googleapis.com/css2?family=Arimo:wght@400;700&family=Archivo+Black&display=swap">
<style>
  :root {
    --band-dark: #85836f;
    --band-mid: #a9a794;
    --band-light: #d2d0c2;
    --ink: #000;
    --text-grey: #5a5a5a;
    --excerpt-grey: #8a8a8a;
    --title-grey: #8f8d7b;
    --tab-label: #b9b7a1;
    --gold-dark: #a8861a;
    --gold-light: #f3dc6a;
    --paper: #fff;
    --rule: #6a6a6a;
    --footer-text: #e6e4d8;
  }
  * { margin: 0; padding: 0; box-sizing: border-box; }
  html, body { width: 1200px; height: 911px; overflow: hidden; background: var(--paper); }
  body { position: relative; font-family: "Arimo", Arial, sans-serif; color: var(--ink); }

  .site-header {
    position: absolute; left: 0; top: 0; width: 1200px; height: 91px;
    background: linear-gradient(90deg, var(--band-dark) 0%, var(--band-light) 18%, var(--band-mid) 40%, var(--band-dark) 100%);
    border-bottom: 1px solid #7a7866;
  }
  .brand-box {
    position: absolute; left: 42px; top: 0; width: 103px; height: 91px; background: #000;
    display: flex; align-items: center; justify-content: center; text-align: center;
  }
  .brand-name { color: var(--band-light); font-weight: 700; font-size: 13px; line-height: 16px; }
  .main-nav { position: absolute; left: 510px; top: 0; height: 91px; display: flex; }
  .main-nav a {
    display: block; width: 248px; height: 91px; padding-top: 47px; text-align: center;
    color: var(--ink); text-decoration: none; font-size: 21px;
    border-left: 1px solid #e4e2d6;
    background: linear-gradient(90deg, rgba(255,255,255,.08), rgba(255,255,255,.35) 50%, rgba(255,255,255,.05));
  }
  .main-nav a:last-child { width: 196px; padding-left: 18px; }

  .hero {
    position: absolute; left: 0; top: 91px; width: 1200px; height: 385px; background: var(--paper);
    border-bottom: 1px solid #ddd;
    box-shadow: 0 6px 10px -6px rgba(0,0,0,.18);
  }
  .hero-title { position: absolute; left: 40px; top: 78px; }
  .hero-glow {
    position: absolute; left: 42px; top: 245px; width: 605px; height: 105px;
    background: linear-gradient(180deg, rgba(0,0,0,.12), rgba(255,255,255,0));
  }
  .hero-art {
    position: absolute; left: 762px; top: 14px; width: 380px; height: 360px;
    background: radial-gradient(ellipse at 50% 35%, var(--gold-light), var(--gold-dark) 55%, rgba(255,255,255,0) 75%);
    opacity: .85;
  }

  .section-tab {
    position: absolute; width: 146px; height: 45px;
    background: linear-gradient(180deg, #3a3a3a, #000 60%);
    border: 3px solid #fff; box-shadow: 0 2px 5px rgba(0,0,0,.45);
    font-family: "Archivo Black", "Arial Black", sans-serif; font-size: 19px; color: var(--tab-label);
    padding: 6px 0 0 13px; text-shadow: 0 1px 1px #000;
  }
  .section-tab::after {
    content: ""; position: absolute; right: 16px; bottom: -13px;
    border-left: 10px solid transparent; border-right: 10px solid transparent; border-top: 11px solid #000;
  }
  .tab-about { left: 46px; top: 500px; }
  .tab-news { left: 736px; top: 500px; }

  .about-copy {
    position: absolute; left: 45px; top: 577px; width: 640px;
    font-size: 15.2px; line-height: 18.3px; letter-spacing: .45px; color: var(--text-grey);
  }
  .column-rule { position: absolute; left: 702px; top: 575px; width: 1px; height: 273px; background: var(--rule); }

  .news-list { position: absolute; left: 751px; top: 583px; width: 378px; }
  .news-list::before, .news-list::after {
    content: ""; position: absolute; left: 20px; width: 330px; height: 8px;
    background: radial-gradient(ellipse at 50% 0, rgba(0,0,0,.25), rgba(0,0,0,0) 70%);
  }
  .news-list::before { top: 0; }
  .news-list::after { top: 264px; }
  .news-item { position: absolute; left: 0; width: 378px; }
  .news-item:nth-child(1) { top: 17px; }
  .news-item:nth-child(2) { top: 135px; }
  .news-date { font-weight: 700; font-size: 14px; letter-spacing: .6px; }
  .news-title { font-weight: 700; font-size: 16px; letter-spacing: 1.7px; margin-top: 2px; }
  .news-excerpt { font-size: 11px; line-height: 14px; letter-spacing: .6px; color: var(--excerpt-grey); margin-top: 9px; }
  .news-more { display: block; text-align: right; font-size: 12px; color: var(--ink); text-decoration: none; margin-top: 15px; }

  .site-footer {
    position: absolute; left: 0; top: 887px; width: 1200px; height: 21px;
    background: linear-gradient(90deg, var(--band-dark), var(--band-light) 45%, var(--band-mid) 70%, var(--band-dark));
    font-size: 9px; color: var(--footer-text);
  }
  .footer-box { position: absolute; left: 42px; top: 0; width: 103px; height: 21px; background: #000; }
  .copyright { position: absolute; left: 156px; top: 5px; word-spacing: 2px; }
  .footer-links { position: absolute; right: 27px; top: 0; display: flex; }
  .footer-links a { color: var(--footer-text); text-decoration: none; padding: 5px 9px 0; height: 21px; border-left: 1px solid #e8e6dc; }
  .footer-links a:first-child { border-left: 0; }
</style>
</head>
<body>
  <header class="site-header">
    <div class="brand-box"><span class="brand-name">Brightwater<br>Digital</span></div>
    <nav class="main-nav">
      <a href="#">Home Page</a>
      <a href="#">Contact Us</a>
      <a href="#">Our Sites</a>
    </nav>
  </header>

  <section class="hero">
    <div class="hero-glow"></div>
    <svg class="hero-title" width="620" height="180" viewBox="0 0 620 180" aria-label="Brightwater Digital">
      <defs>
        <linearGradient id="title-light" x1="0" x2="1">
          <stop offset="0" stop-color="#8b8977"/><stop offset=".5" stop-color="#b3b19f"/><stop offset="1" stop-color="#7c7a69"/>
        </linearGradient>
        <linearGradient id="title-dark" x1="0" x2="1">
          <stop offset="0" stop-color="#111"/><stop offset=".5" stop-color="#4a4a4a"/><stop offset="1" stop-color="#111"/>
        </linearGradient>
      </defs>
      <text x="4" y="166" textLength="603" lengthAdjust="spacingAndGlyphs" font-family="Archivo Black, Arial Black, sans-serif" font-size="138" fill="url(#title-dark)">DIGITAL</text>
      <text x="6" y="54" textLength="578" lengthAdjust="spacingAndGlyphs" font-family="Arimo, Arial, sans-serif" font-size="64" fill="url(#title-light)" opacity=".95">BRIGHTWATER</text>
    </svg>
    <div class="hero-art" role="img" aria-label="Three gold dollar signs of decreasing size with reflections"></div>
  </section>

  <div class="section-tab tab-about">About Us</div>
  <div class="section-tab tab-news">Last News</div>

  <p class="about-copy">Cras neque justo, ultrices at, rhoncus a facilisis eget,nisl. Quisque vitae pede. Nam et augue. Sed a elit. Ut vel massa. Suspendisse nibh pede, ultrices vitae, ultrices nec, mollis non nibh. In sit amet pede quis leo vulputate hendrerit. Cras laoreet leo et justo auctor condimentum. Integer id enim. Suspendisse nibh pede, ultrices vitae, ultrices nec, mollis non, nibh. In sit amet pede quis leo vulputate hendrerit.Cras neque justo, ultrices at, rhoncus a facilisis eget,nisl. Quisque vitae pede. Nam et augue.<br>Sed a elit. Ut vel massa. Suspendisse nibh pede, ultrices vitae, ultrices nec, mollis non nibh. In sit amet pede quis leo vulputate hendrerit.<br>Cras neque justo, ultrices at, rhoncus a facilisis eget,nisl. Quisque vitae pede. Nam et augue. Sed a elit. Ut vel massa. Suspendisse nibh pede, ultrices vitae, ultrices nec, mollis non nibh. In sit amet pede quis leo vulputate hendrerit. Cras laoreet leo et justo auctor condimentum. Integer id enim. Suspendisse nibh pede, ultrices vitae, ultrices nec, mollis non, nibh. In sit amet pede quis leo vulputate hendrerit.Cras neque justo, ultrices at, rhoncus a facilisis eget,nisl. Quisque vitae pede. Nam et augue.</p>

  <div class="column-rule"></div>

  <div class="news-list">
    <article class="news-item">
      <div class="news-date">12.06.2011</div>
      <h3 class="news-title">Quisque vitae pede.</h3>
      <p class="news-excerpt">Quisque vitae pede. Nam et augue.Sed a elit. Ut vel massa. Suspen-<br>dissenibh pede, ultrices vitae,ultrices nec,mollis non nibh...</p>
      <a class="news-more" href="#">Learn more...</a>
    </article>
    <article class="news-item">
      <div class="news-date">12.06.2011</div>
      <h3 class="news-title">Quisque vitae pede.</h3>
      <p class="news-excerpt">Quisque vitae pede. Nam et augue.Sed a elit. Ut vel massa. Suspen-<br>dissenibh pede, ultrices vitae,ultrices nec,mollis non nibh...</p>
      <a class="news-more" href="#">Learn more...</a>
    </article>
  </div>

  <footer class="site-footer">
    <div class="footer-box"></div>
    <span class="copyright">Copyright &nbsp; 2011 All rights reserved</span>
    <nav class="footer-links">
      <a href="#">Contact us</a>
      <a href="#">Terms and Conditions</a>
      <a href="#">Site map</a>
    </nav>
  </footer>
</body>
</html>
```